It is a leisure sector investment company.The company plans to invest in a luxurious 5 star resort

We need a stationery design to our company 'Solmaran Crest Limited' using the winning logo design. We need the letter heads, envelopes & the business cards. Should be simple, plain and professional
Updates
We have upload the source file & vector files which gives our logo design. We prefer the bottom logo.

Have updated under 'must have priorities', the company name, address, tel no. fax no. & the company reg no. which should come on the letter head. the long envelope should have the company name, tel & fax no. 
Business card should have the company name, name on the card, designation, tel no. fax no.  

Industry/Entity Type
Investment
Requirements
Must have
- Letter head details:
Solmaran Crest Limited
14 Floor, North Block, Harbour Meridian Plaza,
Velmont Circus, Colombo 01, Sri Lanka
Tel: +94 11 2764502 Fax: +94 11 2764508
Company Reg No.PB 6192
Long Envelope should have only the company name, adress, Tel & Fax
Business Cards should have the company name, Tel & Fax:
Business Card 1 - Lasantha Wijeratne - Chairman
Business Card 2 - Nuwan.S.Gunawardhana - COO

```html
<!DOCTYPE html>
<html lang="en">
<head>
<meta charset="utf-8">
<title>Solmaran Crest Limited – Business Card</title>
<link rel="stylesheet" href="https://fonts.googleapis.com/css2?family=Gelasio:wght@400&family=Open+Sans:wght@400&display=swap">
<style>
  :root {
    --backdrop: #2a2a2a;
    --card-light: #ffffff;
    --card-edge: #e2e2e2;
    --ink: #1c1c1c;
    --ink-soft: #555555;
    --ink-muted: #777777;
    --rule: #b8b8b8;
    --flourish: rgba(0, 0, 0, 0.045);
  }
  * { margin: 0; padding: 0; box-sizing: border-box; }
  html, body {
    width: 900px; height: 1200px; overflow: hidden;
    background: var(--backdrop);
  }
  .canvas { position: relative; width: 900px; height: 1200px; }
  .card {
    position: absolute;
    background: radial-gradient(ellipse at 60% 55%, var(--card-light) 30%, var(--card-edge) 100%);
    overflow: hidden;
  }
  .card--front { left: 100px; top: 107px; width: 690px; height: 412px; }
  .card--back  { left: 104px; top: 684px; width: 688px; height: 412px; }

  .flourish { position: absolute; border-radius: 50%; }
  .flourish--top    { left: 410px; top: 0; width: 280px; height: 150px;
    background: radial-gradient(ellipse, var(--flourish), transparent 70%); }
  .flourish--bottom { left: 0; top: 260px; width: 310px; height: 152px;
    background: radial-gradient(ellipse, var(--flourish), transparent 70%); }

  .brand {
    position: absolute; font-family: "Gelasio", serif; font-weight: 400;
    font-variant: small-caps; color: var(--ink); text-align: center;
    letter-spacing: 0.02em; line-height: 1.05;
  }
  .card--front .brand { left: 22px; top: 72px; width: 276px; font-size: 29px; }
  .card--back .brand  { left: 0; top: 152px; width: 688px; font-size: 40px; }
  .brand__sub { display: block; font-size: 0.72em; letter-spacing: 0.22em; }

  .holder { position: absolute; left: 137px; top: 174px; font-family: "Gelasio", serif; }
  .holder__name  { font-size: 20px; color: var(--ink); }
  .holder__title { font-size: 15px; color: var(--ink-soft); margin-top: 6px; }

  .contact {
    position: absolute; left: 352px; top: 265px; width: 285px;
    font-family: "Open Sans", sans-serif; color: var(--ink-soft);
  }
  .contact__address { font-size: 12.5px; line-height: 21px; padding: 0 0 3px 2px;
    border-bottom: 1px dashed var(--rule); }
  .contact__lines { padding: 6px 0 6px 0; border-bottom: 1px dashed var(--rule); }
  .contact__row { display: flex; font-size: 14px; line-height: 21px; }
  .contact__label { width: 99px; padding-left: 37px; font-size: 12.5px; color: var(--ink-muted); }

  .reg {
    position: absolute; left: 0; top: 378px; width: 688px; text-align: center;
    font-family: "Open Sans", sans-serif; font-size: 13px; line-height: 18px;
    color: var(--ink-muted);
  }
</style>
</head>
<body>
<main class="canvas">
  <section class="card card--front">
    <div class="flourish flourish--top" role="img" aria-label="Faint decorative flourish pattern"></div>
    <div class="flourish flourish--bottom" role="img" aria-label="Faint decorative flourish pattern"></div>
    <div class="brand">Solmaran Crest<span class="brand__sub">Limited</span></div>
    <div class="holder">
      <p class="holder__name">Lasantha Wijeratne</p>
      <p class="holder__title">Chairman</p>
    </div>
    <div class="contact">
      <p class="contact__address">14 Floor, North Block, Harbour Meridian Plaza,<br>Velmont Circus, Colombo 01, Sri Lanka</p>
      <div class="contact__lines">
        <p class="contact__row"><span class="contact__label">Mobile</span>: +94 713 508 267</p>
        <p class="contact__row"><span class="contact__label">Tel</span>: +94 112 764 502</p>
        <p class="contact__row"><span class="contact__label">Fax</span>: +94 112 764 508</p>
      </div>
    </div>
  </section>

  <section class="card card--back">
    <div class="brand">Solmaran Crest<span class="brand__sub">Limited</span></div>
    <p class="reg">Company Reg No.PB 6192</p>
  </section>
</main>
</body>
</html>
```